Business Card Design

We need a business card design that can also be aplied for postcards. We are a small indie record company that also do consulting, and development of independat artitst . I already have the name and the basic idea of what i am looking for but i am open to any suggestion.
Info for the card
Name of the company : Velmora Records
NAME : Tomas Invaldi
PHONE : 208-5536142
EMAIL : hello@velmorarecords.example
WEB: www.velmorarecords.example
Target Market(s)
Male - Female independent musicians ages 18 to 45
Industry/Entity Type
Record Company
Contact Information for Business Card
Independant records company that also works in consulting for music business models for independent artists
Look and feel
Each slider illustrates characteristics of the customer's brand and the style your logo design should communicate.

```html
<!DOCTYPE html>
<html lang="en">
<head>
<meta charset="utf-8">
<title>Velmora Records — Business Card</title>
<link rel="stylesheet" href="https://fonts.googleapis.com/css2?family=Lato:wght@400;700&display=swap">
<style>
  :root {
    --stage: #e9e9e7;
    --card-white: #ffffff;
    --card-dark: #2a2a2a;
    --ink: #1f1f1f;
    --orange: #f39a1e;
    --orange-deep: #e0841a;
    --muted: #cfcfcf;
  }
  * { box-sizing: border-box; margin: 0; padding: 0; }
  html, body {
    width: 1200px; height: 1200px; overflow: hidden;
    background: var(--stage);
    font-family: "Lato", Arial, sans-serif;
  }
  .canvas {
    width: 1200px; height: 1200px;
    display: flex; flex-direction: column; align-items: center; justify-content: center;
    gap: 70px;
  }
  .card {
    width: 840px; height: 480px;
    position: relative; overflow: hidden;
    box-shadow: 0 10px 30px rgba(0,0,0,0.18);
  }

  /* Front */
  .card--front { background: var(--card-white); }
  .card--front .brand {
    position: absolute; inset: 0 0 40px 0;
    display: flex; align-items: center; justify-content: center; gap: 22px;
  }
  .card--front .brand__mark { width: 44px; height: 44px; background: var(--orange); }
  .card--front .brand__name { font-size: 64px; font-weight: 700; color: var(--ink); letter-spacing: 0.5px; }
  .card--front .edge-band {
    position: absolute; left: 0; right: 0; bottom: 0; height: 40px; background: var(--orange);
  }

  /* Back */
  .card--back { background: var(--card-dark); }
  .card--back .header {
    position: absolute; left: 0; right: 0; top: 0; height: 170px;
    background: var(--card-white);
    display: flex; align-items: center; justify-content: center; gap: 16px;
  }
  .card--back .brand__mark { width: 30px; height: 30px; background: var(--orange); }
  .card--back .brand__name { font-size: 44px; font-weight: 700; color: var(--ink); }
  .card--back .person {
    position: absolute; top: 205px; left: 0; right: 0; text-align: center;
    font-size: 40px; font-weight: 400; color: var(--orange);
  }
  .card--back .contacts {
    position: absolute; top: 300px; left: 60px; right: 60px;
    display: flex; justify-content: space-between; align-items: center;
    color: var(--muted); font-size: 21px;
  }
  .contact { display: flex; align-items: center; gap: 12px; }
  .contact svg { flex: none; }
  .card--back .web {
    position: absolute; top: 380px; left: 0; right: 0; text-align: center;
    font-size: 22px; color: var(--orange); letter-spacing: 0.5px;
  }
  .card--back .edge-band {
    position: absolute; left: 0; right: 0; bottom: 0; height: 22px; background: var(--orange);
  }
</style>
</head>
<body>
<main class="canvas">
  <section class="card card--front" aria-label="Card front">
    <div class="brand">
      <span class="brand__mark"></span>
      <span class="brand__name">Velmora Records</span>
    </div>
    <div class="edge-band"></div>
  </section>

  <section class="card card--back" aria-label="Card back">
    <div class="header">
      <span class="brand__mark"></span>
      <span class="brand__name">Velmora Records</span>
    </div>
    <p class="person">Tomas Invaldi</p>
    <div class="contacts">
      <div class="contact contact--email">
        <svg width="26" height="18" viewBox="0 0 26 18" aria-hidden="true">
          <rect x="0" y="0" width="26" height="18" rx="2" fill="var(--orange)"/>
          <path d="M1 1 L13 10 L25 1" fill="none" stroke="var(--card-dark)" stroke-width="2"/>
        </svg>
        <span>hello@velmorarecords.example</span>
      </div>
      <div class="contact contact--phone">
        <svg width="16" height="26" viewBox="0 0 16 26" aria-hidden="true">
          <rect x="1" y="1" width="14" height="24" rx="2.5" fill="none" stroke="var(--orange)" stroke-width="2"/>
          <rect x="4" y="4" width="8" height="13" fill="var(--orange)"/>
          <circle cx="8" cy="21" r="1.6" fill="var(--orange)"/>
        </svg>
        <span>208-5536142</span>
      </div>
    </div>
    <p class="web">www.velmorarecords.example</p>
    <div class="edge-band"></div>
  </section>
</main>
</body>
</html>
```